New Construction Truck Wrap

I need an awesome vehicle wrap for my Black Vex. This is for a Construction Company in Florida that specializes in Hurricane Restoration. I need the phone number to be on each Vex Bin which needs to be separate pieces of the wrap as they move and I can change phone numbers for different markets. My web address is www.harbelbuilders.net and the phone is 850-555-0148. The truck is a 2016 Vex 2300 Turbo Gasol Quad Cab Premier With Vex Bins. Black and Chrome.

Colors

Designer to choose colors to be used in the design.

Requirements
Must have
• Must stand out and get noticed. This is a marketing tool. I just uploaded my old truck wrap for a different company. I like this design with the storm pictures in back ground if it is possible to incorporate into this design. Also I am going to purchase a white VEX just like the black one so the wrap needs to work on both colors.

```html
<!DOCTYPE html>
<html lang="en">
<head>
<meta charset="utf-8">
<title>Harbel Builders – Vehicle Wrap Panel</title>
<link rel="stylesheet" href="https://fonts.googleapis.com/css2?family=Montserrat:wght@400;700&family=Encode+Sans+Semi+Condensed:wght@500;700&display=swap">
<style>
  :root {
    --navy: #2e3192;
    --red: #ed1c24;
    --white: #ffffff;
  }
  html, body {
    margin: 0;
    padding: 0;
    overflow: hidden;
    background: var(--white);
  }
  .wrap-panel {
    position: relative;
    width: 1200px;
    height: 480px;
    overflow: hidden;
    background: var(--white);
  }
  .wave-art {
    position: absolute;
    inset: 0;
    width: 1200px;
    height: 480px;
  }
  .brand-name {
    position: absolute;
    left: 213px;
    top: 118px;
    width: 300px;
    margin: 0;
    text-align: center;
    font-family: "Montserrat", sans-serif;
    font-weight: 700;
    font-size: 38px;
    line-height: 1.1;
    letter-spacing: 1px;
    color: var(--navy);
    text-transform: uppercase;
  }
  .contact-phone {
    position: absolute;
    left: 146px;
    top: 343px;
    margin: 0;
    font-family: "Montserrat", sans-serif;
    font-weight: 700;
    font-size: 60px;
    line-height: 1;
    letter-spacing: -0.5px;
    color: var(--white);
  }
  .contact-web {
    position: absolute;
    left: 143px;
    top: 418px;
    margin: 0;
    font-family: "Montserrat", sans-serif;
    font-weight: 400;
    font-size: 31px;
    line-height: 1;
    color: var(--white);
  }
  .anniversary {
    position: absolute;
    left: 724px;
    top: 262px;
    width: 420px;
    height: 140px;
    font-family: "Encode Sans Semi Condensed", sans-serif;
  }
  .anniversary-number {
    position: absolute;
    left: 0;
    top: 0;
    font-weight: 700;
    font-size: 158px;
    line-height: 1;
    letter-spacing: -8px;
    color: var(--red);
  }
  .anniversary-year {
    position: absolute;
    left: 129px;
    top: 56px;
    width: 34px;
    height: 19px;
    background: var(--white);
    color: var(--red);
    font-weight: 700;
    font-size: 13px;
    line-height: 19px;
    text-align: center;
    letter-spacing: 0.5px;
  }
  .anniversary-label {
    position: absolute;
    left: 170px;
    top: 10px;
    font-weight: 500;
    font-size: 20px;
    line-height: 1;
    letter-spacing: 3px;
    color: var(--white);
  }
  .anniversary-tagline {
    position: absolute;
    left: 168px;
    top: 28px;
    margin: 0;
    font-weight: 700;
    font-size: 54px;
    line-height: 0.9;
    letter-spacing: -2px;
    color: var(--white);
  }
</style>
</head>
<body>
  <main class="wrap-panel">
    <svg class="wave-art" viewBox="0 0 2084 834" preserveAspectRatio="none" aria-hidden="true">
      <path class="wave-body" fill="var(--navy)"
        d="M0,368 C300,560 700,575 1000,470 C1300,370 1650,310 2084,345 L2084,834 L0,834 Z"/>
      <path class="wave-stripe-left" fill="var(--red)"
        d="M0,405 C200,515 440,572 635,570 C420,600 180,545 0,470 Z"/>
      <path class="wave-stripe-right" fill="var(--red)"
        d="M1230,435 C1500,360 1800,320 2084,345 L2084,402 C1800,365 1500,375 1230,435 Z"/>
    </svg>

    <h1 class="brand-name">Harbel<br>Builders</h1>

    <p class="contact-phone">850-555-0148</p>
    <p class="contact-web">www.harbelbuilders.net</p>

    <div class="anniversary">
      <span class="anniversary-number">20</span>
      <span class="anniversary-year">YEAR</span>
      <span class="anniversary-label">ANNIVERSARY</span>
      <p class="anniversary-tagline"><br>Excellence<br>Service</p>
    </div>
  </main>
</body>
</html>
```